Biotech company website design

We are looking for innovative design of our upcoming website. We are a small biotechnology company in Europe dealing with life science products and services.
Updates

Please incorporate the following top level links:
ABOUT US, PRODUCTS, SERVICES, SUPPLIERS, NEWS AND PROMOS, CONTACT US

Target Market(s)

Science people, hospitals, universities ....

Industry/Entity Type

It Company

Requirements
Must have
• Must incorporate our current logo (its color toning)

```html
<!DOCTYPE html>
<html lang="en">
<head>
<meta charset="utf-8">
<title>VerdaLine Biosystems</title>
<link href="https://fonts.googleapis.com/css2?family=Open+Sans:wght@300;400;600;700&display=swap" rel="stylesheet">
<style>
:root{
  --green:#7cb82f;
  --lime:#b9d530;
  --leaf-dark:#2f6b12;
  --footer:#234b0f;
  --pale:#eef5e6;
  --ink:#333;
  --ink-soft:#666;
  --line:#e2e2e2;
  --black:#000;
}
*{margin:0;padding:0;box-sizing:border-box}
html,body{width:1200px;height:1067px;overflow:hidden;background:#fff}
body{position:relative;font-family:"Open Sans",Arial,sans-serif;color:var(--ink)}
.abs{position:absolute}
.brand{left:258px;top:28px;display:flex;align-items:center;gap:10px}
.brand-mark{width:34px;height:34px;background:var(--lime)}
.brand-name{font-size:18px;font-weight:400;color:var(--leaf-dark)}
.main-nav{left:612px;top:40px;display:flex;gap:24px;font-size:9.5px;color:#555}
.main-nav .current{color:var(--green)}
.header-rule{left:258px;top:73px;width:667px;height:1px;background:var(--line)}
.hero{left:0;top:91px;width:1200px;height:272px;background:var(--black)}
.hero-visual{left:512px;top:91px;width:433px;height:211px;background:radial-gradient(ellipse at 65% 45%,#1aa3b4 0%,#0b4c58 35%,#041518 70%,#000 100%)}
.hero-arrow{top:216px;width:32px;height:32px;border-radius:50%;background:#3a3a3a}
.hero-arrow svg{display:block}
.hero-dots{left:884px;top:286px;display:flex;gap:3px}
.hero-dots span{width:8px;height:8px;border-radius:50%;background:#f2f0c6}
.hero-dots .on{background:var(--green)}
.hero-tagline{left:0;top:320px;width:1200px;text-align:center;font-size:16.5px;color:var(--lime)}
.intro{left:258px;top:364px;width:667px;height:135px;border:1px solid var(--line);border-top:none;border-radius:0 0 6px 6px;box-shadow:0 12px 14px -12px rgba(0,0,0,.25)}
.intro-band{left:0;top:0;width:667px;height:99px;background:var(--pale)}
.intro-photo{left:0;top:0;width:118px;height:99px;background:linear-gradient(135deg,#c9d4dc,#e8dcd3 60%,#b7a395)}
.intro-text{left:151px;top:22px;width:460px;font-size:10px;line-height:16px;color:var(--ink-soft)}
.btn-more{left:571px;top:62px;width:78px;height:25px;border-radius:4px;background:linear-gradient(#3f8a1c,#1d5a0a);color:#fff;font-size:10px;font-weight:700;text-align:center;line-height:25px}
.intro-links{left:18px;top:111px;font-size:10px;color:var(--leaf-dark)}
.intro-links span{position:absolute;white-space:nowrap}
.col-title{font-size:17px;font-weight:300;color:var(--ink);top:530px;white-space:nowrap}
.col-photo{top:569px;height:67px;width:183px;box-shadow:0 10px 10px -8px rgba(0,0,0,.3)}
.col-text{top:655px;width:175px;font-size:8.6px;line-height:16px;color:#222}
.col-text a,.more{color:var(--green);text-decoration:none}
.section-title{left:258px;top:738px;font-size:17px;font-weight:300}
.section-text{left:258px;top:766px;width:430px;font-size:8.6px;line-height:16px;color:#222}
.section-photo{left:258px;top:837px;width:425px;height:61px;background:linear-gradient(90deg,#cdb9a4,#e9dcd0 40%,#6b8f3a 50%,#e5d4c4 62%,#bfa48c)}
.news{left:742px;top:730px;width:183px;height:188px;background:var(--pale);border:1px solid #d6e3c8;border-radius:6px;box-shadow:0 12px 12px -12px rgba(0,0,0,.3)}
.news h3{position:absolute;left:8px;top:8px;font-size:17px;font-weight:300;color:var(--ink)}
.news-item{position:absolute;left:9px;width:160px;font-size:8.3px;line-height:12.5px;color:var(--green)}
.news-item time{display:block;margin-top:6px;color:#333;font-size:7.5px}
.news-divider{position:absolute;left:9px;top:101px;width:160px;height:1px;background:#dbe6cf}
.footer{left:0;top:933px;width:1200px;height:134px;background:var(--footer);color:#fff}
.footer h4{position:absolute;top:19px;font-size:16px;font-weight:400}
.footer-photo{left:258px;top:48px;width:82px;height:60px;border:3px solid #fff;transform:rotate(2deg);background:radial-gradient(circle at 50% 50%,#2aa7a0,#163f5c 70%)}
.footer-text{left:364px;top:51px;width:190px;font-size:8.3px;line-height:12px}
.footer-more{left:364px;top:102px;font-size:8.3px;font-weight:700}
.social{top:49px;width:16px;height:16px;border-radius:2px;background:#6a8fbf}
.tweet{left:576px;top:77px;width:166px;height:46px;background:#5aa02c;border-radius:6px;font-size:8.3px;line-height:10.5px;padding:6px 9px}
.tweet::before{content:"";position:absolute;left:36px;top:-6px;border:6px solid transparent;border-top:0;border-bottom-color:#5aa02c}
.tweet .handle{font-size:9px;margin-bottom:5px}
.footer-brand{right:275px;top:39px;display:flex;align-items:center;gap:6px;font-size:10px}
.footer-brand i{width:16px;height:16px;background:#fff;display:block}
.footer-copy{right:275px;top:66px;text-align:right;font-size:7.5px;color:#c9d6c0;line-height:10px}
</style>
</head>
<body>
<header>
  <div class="abs brand"><span class="brand-mark"></span><span class="brand-name">VerdaLine Biosystems</span></div>
  <nav class="abs main-nav"><span class="current">Lorem Ipsum</span><span>Lorem Ipsum</span><span>Lorem Ipsum</span><span>Lorem Ipsum</span><span>Lorem Ipsum</span></nav>
  <div class="abs header-rule"></div>
</header>

<section>
  <div class="abs hero"></div>
  <div class="abs hero-visual" role="img" aria-label="Glowing turquoise DNA double helix on black"></div>
  <div class="abs hero-arrow" style="left:258px"><svg width="32" height="32"><path d="M9 16l7-7v5h7v4h-7v5z" fill="#9a9a9a"/></svg></div>
  <div class="abs hero-arrow" style="left:892px"><svg width="32" height="32"><path d="M23 16l-7-7v5H9v4h7v5z" fill="#9a9a9a"/></svg></div>
  <div class="abs hero-dots"><span class="on"></span><span></span><span></span><span></span></div>
  <p class="abs hero-tagline">Lorem Ipsum is simply dummy text of the printing and typesetting industry.</p>
</section>

<section class="abs intro">
  <div class="abs intro-band"></div>
  <div class="abs intro-photo" role="img" aria-label="Scientist studying a molecular model"></div>
  <p class="abs intro-text">Lorem Ipsum is simply dummy text of the printing and typesetting industry. Lorem Ipsum has been the industry's standard dummy text ever since the 1500s, when an unknown printer took a galley of type and scrambled it to make a type specimen book.</p>
  <div class="abs btn-more">+view more</div>
  <div class="abs intro-links"><span style="left:0">&gt;&gt;Lorem Ipsum</span><span style="left:92px">&gt;&gt;Lorem Ipsum</span><span style="left:183px">&gt;&gt;Lorem Ipsum</span><span style="left:278px">&gt;&gt;Lorem Ipsum</span><span style="left:380px">&gt;&gt;Lorem Ipsum</span></div>
</section>

<section>
  <h2 class="abs col-title" style="left:258px">Lorem Ipsum is simply</h2>
  <h2 class="abs col-title" style="left:500px">Lorem Ipsum is simply</h2>
  <h2 class="abs col-title" style="left:742px">Lorem Ipsum is simply</h2>
  <div class="abs col-photo" style="left:258px;height:80px;box-shadow:none;background:linear-gradient(90deg,#c4234a 0%,#d85a2a 30%,#0e5a73 32%,#1a8aa0 70%,#0b2e48)" role="img" aria-label="Colourful cells and molecular network"></div>
  <div class="abs col-photo" style="left:500px;background:linear-gradient(90deg,#6c9b3e,#b49888 40%,#c7a596 60%,#5c5a4e)" role="img" aria-label="Lab plants in test tubes and flowers"></div>
  <div class="abs col-photo" style="left:743px;background:linear-gradient(90deg,#6c9b3e,#b49888 40%,#c7a596 60%,#5c5a4e)" role="img" aria-label="Lab plants in test tubes and flowers"></div>
  <p class="abs col-text" style="left:267px">Lorem Ipsum is simply dummy text of the printing and typesetting industry. Lorem Ipsum has been the industry's.. <a>+view more</a></p>
  <p class="abs col-text" style="left:509px">Lorem Ipsum is simply dummy text of the printing and typesetting industry. Lorem Ipsum has been the industry's.. <a>+view more</a></p>
  <p class="abs col-text" style="left:751px">Lorem Ipsum is simply dummy text of the printing and typesetting industry. Lorem Ipsum has been the industry's.. <a>+view more</a></p>
</section>

<section>
  <h2 class="abs section-title">Lorem Ipsum is simply</h2>
  <p class="abs section-text">Lorem Ipsum is simply dummy text of the printing and typesetting industry. Lorem Ipsum has been the industry's standard dummy text ever since the 1500s, when an unknown printer took a galley of type and scrambled it to make a type specimen book. It has survived not only five centuries, but also the leap into electronic typesetting, remaining essentially unchanged. It was popularised in the 1960s with the release</p>
  <div class="abs section-photo" role="img" aria-label="Hands holding a seedling in soil"></div>
</section>

<aside class="abs news">
  <h3>News Update</h3>
  <div class="news-item" style="top:42px">&gt;&gt; Lorem Ipsum is simply dummy text of the printing and typesetting industry. Lorem Ipsum has been the industry's standard<time>September 26, 2013</time></div>
  <div class="news-divider"></div>
  <div class="news-item" style="top:112px">&gt;&gt; Lorem Ipsum is simply dummy text of the printing and typesetting industry. Lorem Ipsum has been the industry's standard<time>September 26, 2013</time></div>
</aside>

<footer class="abs footer">
  <h4 style="left:258px">Lorem Ipsum</h4>
  <div class="abs footer-photo" role="img" aria-label="Blue molecular network"></div>
  <p class="abs footer-text">Lorem Ipsum is simply dummy text of the printing and typesetting industry. Lorem Ipsum has been the industry's standard dummy text ever since the 1500s, when an unknown</p>
  <div class="abs footer-more">+view more</div>
  <h4 style="left:576px">Lorem Ipsum</h4>
  <span class="abs social" style="left:576px"></span>
  <span class="abs social" style="left:609px;background:#5fb0d8"></span>
  <span class="abs social" style="left:641px;background:#d9d9d9"></span>
  <div class="abs tweet"><div class="handle">@abc/tweet/http://abc</div>Lorem Ipsum is simply dummy text of the printing and typesetting industry</div>
  <div class="abs footer-brand"><i></i>VerdaLine Biosystems</div>
  <p class="abs footer-copy">2013 All Right Reserved VerdaLine Biosystems</p>
</footer>
</body>
</html>
```